6 page (for now) squarespace website design for a Mobile Fitness small business

My sons California based small business "Brindle Motion Coaching" with new subsidiary called "Brindle Motion 4 Kids". I don't understand coding the website, is that the function squarespace provides?
In the end I want a working website, squarespace, I have a google workspace domain, email and subscription to squarespace & google workspace. URLs include brindlemotioncoaching.example and brindlemotion4kids.example. I have an idea of what I am looking for in a website and I have some examples of website designs I like, but I am 100% open to your design concepts and artistic flair. email is corwin@brindlemotioncoaching.example
I am looking for someone to design the site, help me understand how to make "minor" changes and hopefully have a long term relationship on the tech side of the business. I need an Idea of pricing for future changes (Rate T&M).
There are 2 businesses so I need a way to incorporate both the main company and a subsidiary into 1 website or link it somehow. I am open to your suggestions how to accomplish that. Do I need 2 completely separate websites or can it be done on 1 site directing you to different pages. I read conflicting info if it is a BAD idea to link 2 different websites so I will defer to your advice.
Below are the pages I need designed:
- Home Page- Brindle Motion Coaching
- Home Page- Brindle Motion 4 Kids (Homeschool market)
- Member Page (subscription service?)
- Workouts- with video clips 1-6 min each
- About
- Contact
- FAQ's
Future work & page designs:
- Store with training subscriptions & a few merch items
- Booking Appointments
- Bookshelf
- email campaign
-Blog
I like the feel of this website:
https://quellpace.example/

```html
<!DOCTYPE html>
<html lang="en">
<head>
<meta charset="utf-8">
<title>Brindle Motion Coaching</title>
<link href="https://fonts.googleapis.com/css2?family=Montserrat:wght@400;500;600&display=swap" rel="stylesheet">
<style>
:root{
  --ink:#111111;
  --text:#333333;
  --muted:#4a4a4a;
  --band:#ebebeb;
  --white:#ffffff;
  --photo-warm:#9a7a62;
  --photo-warm-2:#cbb49e;
  --photo-cool:#5f6870;
  --photo-cool-2:#a9b0b6;
}
*{margin:0;padding:0;box-sizing:border-box}
html,body{width:1200px;height:4183px;overflow:hidden}
body{font-family:"Montserrat",sans-serif;color:var(--ink);background:var(--white);position:relative}
.section{position:absolute;left:0;width:1200px}
.band{background:var(--band)}
.abs{position:absolute}
.photo{position:absolute}
.warm{background:linear-gradient(160deg,var(--photo-warm-2),var(--photo-warm) 60%,#5e4a3c)}
.cool{background:linear-gradient(160deg,var(--photo-cool-2),var(--photo-cool) 60%,#3b4248)}
.btn{position:absolute;background:var(--ink);color:var(--white);font-weight:600;font-size:17px;display:flex;align-items:center;justify-content:center;text-decoration:none;white-space:nowrap}

/* header */
.site-header{top:0;height:90px}
.brand{position:absolute;left:110px;top:24px;display:flex;align-items:center;gap:12px}
.brand-mark{width:44px;height:44px;border-radius:50%;background:var(--ink)}
.brand-name{font-size:15px;font-weight:500;letter-spacing:2px;color:var(--ink);white-space:nowrap}
.nav a{position:absolute;top:36px;font-size:15px;color:var(--text);text-decoration:none;text-transform:uppercase;white-space:nowrap}
.nav a.active{border-bottom:1px solid var(--ink);padding-bottom:5px}
.social-dot{position:absolute;width:14px;height:14px;border-radius:50%;background:var(--ink)}

/* hero */
.hero{top:0;height:663px}
.hero-kicker{left:658px;top:205px;font-size:19px;font-weight:500;white-space:nowrap}
.hero-title{left:658px;top:240px;font-size:27px;font-weight:600;line-height:38px;white-space:nowrap}

/* sections */
.section-title{width:1200px;text-align:center;font-size:31px;font-weight:500}
.section-intro{width:1200px;text-align:center;font-size:17px;line-height:26px;color:var(--text)}
.card-title{font-size:26px;font-weight:500;white-space:nowrap}
.card-text{font-size:14.5px;line-height:21px;color:var(--muted);width:300px}
.card-link{font-size:15px;color:var(--ink);text-decoration:underline}

.about-title{left:635px;top:1875px;font-size:29px;font-weight:500}
.about-text{left:635px;top:1918px;width:460px;font-size:17px;line-height:29px;color:var(--text)}

.play{position:absolute;left:542px;top:3646px;width:114px;height:114px}
.footer-note{top:4085px;width:1200px;text-align:center;font-size:16px;font-weight:500}
</style>
</head>
<body>

<section class="section band hero">
  <header class="site-header">
    <div class="brand"><span class="brand-mark"></span><span class="brand-name">BRINDLE MOTION</span></div>
    <nav class="nav">
      <a class="active" style="left:367px">Home</a>
      <a style="left:447px">About</a>
      <a style="left:531px">Blog</a>
      <a style="left:606px">Member</a>
      <a style="left:706px">Workout</a>
      <a style="left:815px">FAQ</a>
      <a style="left:877px">Contact</a>
    </nav>
    <span class="social-dot" style="left:975px;top:35px" aria-label="Social link"></span>
    <span class="social-dot" style="left:1024px;top:35px" aria-label="Social link"></span>
    <span class="social-dot" style="left:1072px;top:35px" aria-label="Social link"></span>
  </header>
  <div class="photo warm" style="left:110px;top:146px;width:489px;height:435px" role="img" aria-label="Coach training a client on suspension straps in a brick-walled gym"></div>
  <p class="abs hero-kicker">Brindle Motion Coaching For Kids</p>
  <h1 class="abs hero-title">Nemo enim ips volupm quia<br>voluptas sit asprtur aut odit<br>autfugit, sed quia consur ni<br>dolores eos qui ratione volm<br>sequi nesciunt.</h1>
  <a class="btn" style="left:658px;top:453px;width:199px;height:67px;font-size:13px">Brindle Motion Coaching</a>
  <a class="btn" style="left:882px;top:453px;width:198px;height:67px;font-size:13px">Brindle Motion 4 Kids</a>
</section>

<section class="section" style="top:663px;height:1026px">
  <h2 class="abs section-title" style="top:88px">Subscription Service</h2>
  <p class="abs section-intro" style="top:146px">Quis autem vel eum iure reprehenderit qui in ea voluptate velit esse quam nihil<br>molestiae consequatur, vel illum qui dolorem&nbsp; nulla pariatur.</p>
</section>
<div class="photo warm" style="left:110px;top:922px;width:306px;height:384px" role="img" aria-label="Trainer coaching a client on a stationary bike"></div>
<h3 class="abs card-title" style="left:108px;top:1323px">Personal Training</h3>
<p class="abs card-text" style="left:110px;top:1368px">Excepteur sint occaecat cupidatat non proident, sunt in culpa.</p>
<a class="abs card-link" style="left:110px;top:1422px">Read More</a>

<div class="photo warm" style="left:448px;top:922px;width:306px;height:249px" role="img" aria-label="Woman holding a plank in front of a laptop at home"></div>
<h3 class="abs card-title" style="left:446px;top:1188px">Online Training</h3>
<p class="abs card-text" style="left:448px;top:1233px">Excepteur sint occaecat cupidatat non proident, sunt in culpa.</p>
<a class="abs card-link" style="left:448px;top:1288px">Read More</a>

<div class="photo cool" style="left:784px;top:922px;width:306px;height:436px" role="img" aria-label="Hand holding a phone showing a workout app"></div>
<h3 class="abs card-title" style="left:782px;top:1376px">Offline Training</h3>
<p class="abs card-text" style="left:784px;top:1421px">Excepteur sint occaecat cupidatat non proident, sunt in culpa.</p>
<a class="abs card-link" style="left:784px;top:1476px">Read More</a>
<a class="btn" style="left:505px;top:1541px;width:188px;height:67px">Subscription</a>

<section class="section band" style="top:1689px;height:659px">
  <div class="photo warm" style="left:110px;top:97px;width:460px;height:470px" role="img" aria-label="Smiling group exercising on spin bikes"></div>
</section>
<h2 class="abs about-title">About</h2>
<p class="abs about-text">Nemo enim ipsam volem quia voluptas sit aspnatur aut odit aut fugit, sed quia consuntur magni dolores eos qui ratione votatem sequi nesciunt. Neque porro quisqem est, qui dolorem ipsum quia dolor sit amet, consectetur, adipisci velit,minima.</p>
<a class="btn" style="left:635px;top:2095px;width:234px;height:66px">Booking Appointments</a>
<a class="btn" style="left:887px;top:2095px;width:156px;height:66px">Bookshelf</a>

<section class="section" style="top:2348px;height:1023px">
  <h2 class="abs section-title" style="top:88px">Recent Blog</h2>
  <p class="abs section-intro" style="top:146px">Quis autem vel eum iure reprehenderit qui in ea voluptate velit esse quam nihil<br>molestiae consequatur, vel illum qui dolorem&nbsp; nulla pariatur.</p>
</section>
<div class="photo warm" style="left:112px;top:2604px;width:306px;height:384px" role="img" aria-label="Group lifting dumbbells overhead in a gym"></div>
<h3 class="abs card-title" style="left:110px;top:3005px">Finibus Bonorum</h3>
<p class="abs card-text" style="left:112px;top:3050px">Excepteur sint occaecat cupidatat non proident, sunt in culpa.</p>
<a class="abs card-link" style="left:112px;top:3104px">Read More</a>

<div class="photo warm" style="left:450px;top:2604px;width:306px;height:249px" role="img" aria-label="Fitness class doing lunges in a bright studio"></div>
<h3 class="abs card-title" style="left:448px;top:2870px">Malorum</h3>
<p class="abs card-text" style="left:450px;top:2915px">Excepteur sint occaecat cupidatat non proident, sunt in culpa.</p>
<a class="abs card-link" style="left:450px;top:2970px">Read More</a>

<div class="photo cool" style="left:786px;top:2604px;width:306px;height:436px" role="img" aria-label="Trainer reviewing a clipboard plan with a client"></div>
<h3 class="abs card-title" style="left:784px;top:3058px">Voluptatem Accusanti</h3>
<p class="abs card-text" style="left:786px;top:3103px">Excepteur sint occaecat cupidatat non proident, sunt in culpa.</p>
<a class="abs card-link" style="left:786px;top:3158px">Read More</a>
<a class="btn" style="left:507px;top:3223px;width:188px;height:67px">Email Campaign</a>

<section class="section band" style="top:3371px;height:812px">
  <div class="photo" style="left:110px;top:96px;width:980px;height:471px;background:linear-gradient(120deg,#8d8f93,#6b6d71 45%,#a0785a 80%,#7c5c44)" role="img" aria-label="Video still of two people doing push-ups in a gym"></div>
</section>
<svg class="play" viewBox="0 0 114 114" aria-label="Play video">
  <circle cx="57" cy="57" r="57" fill="#1a1a1a" fill-opacity="0.75"/>
  <polygon points="46,38 46,76 78,57" fill="#ffffff"/>
</svg>
<span class="social-dot" style="left:520px;top:4031px" aria-label="Social link"></span>
<span class="social-dot" style="left:591px;top:4031px" aria-label="Social link"></span>
<span class="social-dot" style="left:661px;top:4031px" aria-label="Social link"></span>
<p class="abs footer-note">Copyrights@2022.All Rights Reserved</p>

</body>
</html>
```